Young Accounting firm needing a captivating business card

We need a business card design that forces the person to look at the card because its either gold foil, plastic, or lettering pop up etc. We already have a logo with a specific gold color and we need to make it pop. We are an accounting firm. I need the words" accounting, payroll, licenses, audits, taxes" somewhere on the business card so as to describe what we do- preferably on the side where the logo is at.

Industry/Entity Type

Accounting

Contact Information for Business Card

Address 48276 9th Ave S Ste 305, Alder Crest, OR 98117
Business Phone (360)418-2096
Fax (360)418-2157
Office Cell Phone (360)586-7319

Font styles to use
Serif

Colors
85abd2

Requirements
Must have
• It should state
• "Accounting" "Taxes" "Audits" "Licenses" "Payroll"
Nice to have
• Matte with gold foil, different textures, With Either a textured ivory background or gray blue slate background
Should not have
• colorful colors

```html
<!DOCTYPE html>
<html lang="en">
<head>
<meta charset="utf-8">
<title>Halvorsen Ledger — Business Card</title>
<link rel="stylesheet" href="https://fonts.googleapis.com/css2?family=Libre+Caslon+Text:wght@400;700&display=swap">
<style>
  :root {
    --page-bg: #f2f2f4;
    --navy: #06304a;
    --gold: #c9a43a;
    --cream: #f1ead8;
    --slate-blue: #85abd2;
    --slate-blue-light: #a9c3e2;
    --ink: #0f2a40;
  }
  * { margin: 0; padding: 0; box-sizing: border-box; }
  html, body { width: 1200px; height: 961px; overflow: hidden; }
  body {
    background: var(--page-bg);
    font-family: "Libre Caslon Text", Georgia, serif;
    position: relative;
  }
  .card {
    position: absolute;
    box-shadow: 0 10px 24px rgba(20, 30, 50, 0.18);
  }
  .card-front {
    left: 128px;
    top: 214px;
    width: 524px;
    height: 324px;
    z-index: 2;
    background: var(--navy);
    display: flex;
    flex-direction: column;
    align-items: center;
    justify-content: center;
  }
  .brand-mark {
    width: 60px;
    height: 60px;
    background: var(--gold);
    margin-bottom: 22px;
  }
  .brand-name {
    color: var(--gold);
    font-weight: 700;
    font-size: 42px;
    letter-spacing: 0.5px;
    line-height: 1;
  }
  .services {
    margin-top: 20px;
    color: var(--cream);
    font-size: 17px;
    letter-spacing: 0.3px;
  }
  .card-back {
    left: 557px;
    top: 423px;
    width: 520px;
    height: 320px;
    z-index: 1;
    overflow: hidden;
  }
  .back-pattern {
    position: absolute;
    inset: 0;
    background: linear-gradient(120deg, var(--slate-blue-light) 0%, var(--slate-blue) 55%, var(--slate-blue-light) 100%);
  }
  .contact {
    position: absolute;
    left: 46px;
    top: 128px;
    bottom: 26px;
    padding-left: 24px;
    border-left: 2px solid var(--ink);
    color: var(--ink);
    font-size: 16px;
    line-height: 1.4;
    list-style: none;
    display: flex;
    flex-direction: column;
    justify-content: center;
    gap: 8px;
  }
</style>
</head>
<body>
  <section class="card card-front" aria-label="Business card front">
    <div class="brand-mark" aria-hidden="true"></div>
    <h1 class="brand-name">Halvorsen Ledger</h1>
    <p class="services">Accounting · Payroll · Licenses · Audits · Taxes</p>
  </section>

  <section class="card card-back" aria-label="Business card back">
    <div class="back-pattern" role="img" aria-label="Repeating pattern of light hexagonal brand shapes on slate blue"></div>
    <ul class="contact">
      <li>48276 9th Ave S Ste 305, Alder Crest, OR 98117</li>
      <li>Business Phone (360)418-2096</li>
      <li>Fax (360)418-2157</li>
      <li>Office Cell Phone (360)586-7319</li>
      <li>office@halvorsenledger.com</li>
    </ul>
  </section>
</body>
</html>
```